Lumo Stack - Powerpoint Templates

We are a consultancy to help builders to optimize their planning in order to save building costs. For that reason we need templates for teasers and presentations where we offer our services, show our team and their capacities and present workflows, organization charts, price lists etc.

```html
<!DOCTYPE html>
<html lang="en">
<head>
<meta charset="utf-8">
<title>Lumo Stack – Presentation Template</title>
<link href="https://fonts.googleapis.com/css2?family=Lexend:wght@400;600;700&family=Montserrat:wght@400;500;600;700&display=swap" rel="stylesheet">
<style>
:root{
  --gold:#d6a23e;
  --gold-light:#e9c272;
  --gold-dark:#a97a22;
  --ink:#2b2b33;
  --navy:#1f1d3a;
  --text:#3a3a3a;
  --paper:#f7f7f8;
  --stage-top:#c3c8ca;
  --stage-bottom:#adafb1;
  --sky-top:#2f72c9;
  --sky-bottom:#bcd6ee;
  --grass:#5d7a2a;
  --city:#c9cbce;
}
*{margin:0;padding:0;box-sizing:border-box}
html,body{width:1200px;height:2301px;overflow:hidden}
body{position:relative;font-family:"Montserrat",sans-serif;color:var(--text);background:var(--stage-bottom)}
.stage-top{position:absolute;left:0;top:0;width:1200px;height:630px;background:var(--stage-top)}
.slide{position:absolute;width:545px;height:280px;background:var(--paper);overflow:hidden;box-shadow:0 10px 18px rgba(0,0,0,.18)}
.slide-hero{left:320px;top:170px;width:560px;height:288px}
.c1{left:48px}.c2{left:615px}
.r1{top:693px}.r2{top:1005px}.r3{top:1326px}.r4{top:1643px}.r5{top:1961px}
.abs{position:absolute}
.wedge{position:absolute;left:0;top:0}
.num{position:absolute;left:20px;top:10px;width:24px;height:22px;background:var(--ink);color:var(--gold-light);font:600 15px/22px "Lexend",sans-serif;text-align:center}
.slide-title{position:absolute;left:54px;top:9px;font:600 16px "Lexend",sans-serif;letter-spacing:1px;color:var(--gold);text-transform:uppercase}
.brand-tag{position:absolute;right:0;top:12px;width:155px;height:30px;background:var(--ink);clip-path:polygon(8% 0,100% 0,100% 100%,0 100%);color:#fff;font:700 11px/30px "Lexend",sans-serif;letter-spacing:.5px;padding-left:36px}
.brand-tag::before{content:"";position:absolute;left:20px;top:10px;width:10px;height:10px;background:var(--gold)}
.footer{position:absolute;right:0;bottom:0;width:120px;height:9px;background:var(--gold);clip-path:polygon(6% 0,100% 0,100% 100%,0 100%);font:600 5px/9px "Montserrat",sans-serif;color:var(--ink);text-align:center}
.skyline{position:absolute;left:0;bottom:0;width:100%;height:62px;background:linear-gradient(to top,var(--city),rgba(201,203,206,0))}
.lorem{font-size:6.5px;line-height:1.35;color:var(--text)}
.photo{position:absolute;background:linear-gradient(160deg,#8aa1b5,#c9b28a)}
/* cover */
.hero-sky{position:absolute;inset:0;background:linear-gradient(to bottom,var(--sky-top),var(--sky-bottom) 70%,#e7eef3)}
.hero-grass{position:absolute;left:0;bottom:0;width:100%;height:34px;background:var(--grass)}
.hero-photo{position:absolute;right:0;top:0;width:50%;height:100%;background:linear-gradient(170deg,#4b79b8 0%,#3f4a5a 45%,#a98a5b 75%,#9c9a94 100%)}
.hero-name{position:absolute;display:flex;align-items:center;gap:8px;font:700 23px "Lexend",sans-serif;color:var(--gold);letter-spacing:1px}
.hero-name::before{content:"";width:14px;height:14px;background:var(--gold)}
.hero-tagline{position:absolute;font:600 9px "Montserrat",sans-serif;color:var(--gold);letter-spacing:2px;text-transform:uppercase}
.hero-url{position:absolute;font:700 12px "Montserrat",sans-serif;color:#fff;letter-spacing:1px}
/* shared text bits */
h3.gold{font:700 7px "Montserrat",sans-serif;color:var(--gold)}
.role{font:600 10px "Lexend",sans-serif;letter-spacing:1.5px;color:var(--gold);text-align:center}
.btn{position:absolute;background:var(--gold);color:#fff;font:500 6px/14px "Montserrat",sans-serif;text-align:center;border-radius:7px}
.bar-label{position:absolute;height:26px;background:linear-gradient(90deg,var(--gold),var(--gold-light));clip-path:polygon(0 0,100% 0,93% 100%,0 100%);font:700 11px/26px "Lexend",sans-serif;color:var(--ink);letter-spacing:1px}
.list-item{position:absolute;left:275px;font:500 9.5px "Montserrat",sans-serif;color:var(--ink)}
.list-item b{display:inline-block;width:16px;height:16px;margin-right:10px;background:var(--gold);color:var(--ink);text-align:center;font:700 10px/16px "Lexend",sans-serif;vertical-align:middle}
.icon-box{position:absolute;width:32px;height:32px;background:var(--ink)}
.stat{position:absolute;font:700 34px "Lexend",sans-serif;color:var(--navy)}
.stat-cap{position:absolute;font:600 9.5px "Montserrat",sans-serif;color:var(--navy)}
.quote-box{position:absolute;width:195px;height:74px;background:var(--gold);border:2px solid #fff;outline:2px solid var(--gold);color:#fff;padding:8px 12px}
.quote-box strong{display:block;font:700 10px "Montserrat",sans-serif;margin-bottom:4px}
.quote-box p{font-size:6.5px;line-height:1.35}
.contact{position:absolute;left:30px;font:500 14px "Montserrat",sans-serif;color:var(--ink);display:flex;align-items:center;gap:10px}
.contact i{display:inline-block;width:18px;height:18px;border-radius:50%;background:var(--navy);flex:none}
.thanks{position:absolute;left:120px;bottom:8px;width:375px;height:30px;background:linear-gradient(90deg,var(--gold-dark),var(--gold),var(--gold-light));clip-path:polygon(5% 0,100% 0,95% 100%,0 100%);font:700 17px/30px "Lexend",sans-serif;letter-spacing:1.5px;color:#fff;text-align:center}
</style>
</head>
<body>

<div class="stage-top"></div>

<!-- featured cover slide -->
<section class="slide slide-hero">
  <div class="hero-sky"></div>
  <div class="hero-grass"></div>
  <div class="hero-photo" role="img" aria-label="Photo of a modern family home with lit double garage at dusk"></div>
  <div class="hero-name" style="left:30px;top:210px">LUMO STACK</div>
  <div class="hero-tagline" style="left:52px;top:240px">Build smart, spend less</div>
  <div class="hero-url" style="left:62px;top:266px">www.website.com</div>
</section>

<!-- 1 cover -->
<section class="slide c1 r1">
  <div class="hero-sky"></div>
  <div class="hero-grass" style="height:30px"></div>
  <div class="hero-photo" role="img" aria-label="Photo of a modern family home with lit double garage at dusk"></div>
  <div class="hero-name" style="left:16px;top:204px;font-size:21px">LUMO STACK</div>
  <div class="hero-tagline" style="left:38px;top:233px;font-size:8.5px">Build smart, spend less</div>
  <div class="hero-url" style="left:55px;top:261px">www.website.com</div>
</section>

<!-- 2 services -->
<section class="slide c2 r1">
  <svg class="wedge" width="60" height="60"><polygon points="0,0 60,0 14,55 0,55" fill="var(--gold)"/></svg>
  <div class="num">2</div><div class="slide-title">Services</div>
  <div class="brand-tag">LUMO STACK</div>
  <div class="abs" style="left:33px;top:88px;font:600 18px 'Lexend',sans-serif;color:var(--ink)">Our Excellency</div>
  <p class="lorem abs" style="left:33px;top:124px;width:165px">Lorem ipsum dolor sit amet, consectetur adipiscing elit. Fusce consectetur odio vitae tempor tincidunt. Quisque ex risus, eleifend aliquet elit</p>
  <div class="btn" style="left:33px;top:175px;width:80px">LEARN MORE</div>
  <svg class="abs" style="left:240px;top:40px" width="70" height="220">
    <line x1="35" y1="0" x2="35" y2="220" stroke="var(--gold)" stroke-width="1.2"/>
    <g fill="var(--gold)" stroke="#fff" stroke-width="3">
      <circle cx="35" cy="40" r="27"/><circle cx="35" cy="97" r="27"/><circle cx="35" cy="168" r="27"/>
    </g>
    <circle cx="35" cy="37" r="6" fill="none" stroke="#fff" stroke-width="2"/><rect x="32" y="44" width="6" height="4" fill="#fff"/>
    <rect x="26" y="88" width="14" height="18" fill="none" stroke="#fff" stroke-width="2"/><circle cx="44" cy="101" r="5" fill="none" stroke="#fff" stroke-width="2"/>
    <rect x="24" y="170" width="4" height="8" fill="#fff"/><rect x="31" y="165" width="4" height="13" fill="#fff"/><rect x="38" y="160" width="4" height="18" fill="#fff"/>
  </svg>
  <p class="lorem abs" style="left:310px;top:68px;width:175px">Lorem ipsum dolor sit amet, consectetur adipiscing elit. Fusce consectetur odio vitae tempor tincidunt. Quisque ex risus, eleifend aliquet elit</p>
  <p class="lorem abs" style="left:310px;top:126px;width:175px">Lorem ipsum dolor sit amet, consectetur adipiscing elit. Fusce consectetur odio vitae tempor tincidunt. Quisque ex risus, eleifend aliquet elit</p>
  <p class="lorem abs" style="left:310px;top:196px;width:175px">Lorem ipsum dolor sit amet, consectetur adipiscing elit. Fusce consectetur odio vitae tempor tincidunt. Quisque ex risus, eleifend aliquet elit</p>
  <div class="footer">www.website.com</div>
</section>

<!-- 3 team -->
<section class="slide c1 r2">
  <svg class="wedge" width="60" height="60"><polygon points="0,0 60,0 14,55 0,55" fill="var(--gold)"/></svg>
  <div class="num">3</div><div class="slide-title">Our Team</div>
  <div class="brand-tag">LUMO STACK</div>
  <svg class="abs" style="left:0;top:80px" width="545" height="20">
    <line x1="90" y1="5" x2="462" y2="5" stroke="var(--ink)" stroke-width="1.5"/>
    <g stroke="var(--ink)" stroke-width="1.5"><line x1="90" y1="5" x2="90" y2="15"/><line x1="214" y1="5" x2="214" y2="15"/><line x1="338" y1="5" x2="338" y2="15"/><line x1="462" y1="5" x2="462" y2="15"/></g>
  </svg>
  <div class="photo" style="left:52px;top:106px;width:76px;height:76px;border-radius:50%" role="img" aria-label="Portrait of the designer"></div>
  <div class="photo" style="left:176px;top:106px;width:76px;height:76px;border-radius:50%" role="img" aria-label="Portrait of the creative lead"></div>
  <div class="photo" style="left:300px;top:106px;width:76px;height:76px;border-radius:50%" role="img" aria-label="Portrait of the marketing lead"></div>
  <div class="photo" style="left:424px;top:106px;width:76px;height:76px;border-radius:50%" role="img" aria-label="Portrait of the operations lead"></div>
  <div class="role abs" style="left:40px;top:188px;width:100px">DESIGNER</div>
  <div class="role abs" style="left:164px;top:188px;width:100px">CREATIVE</div>
  <div class="role abs" style="left:288px;top:188px;width:100px">MARKETING</div>
  <div class="role abs" style="left:412px;top:188px;width:100px">OPERATION</div>
  <p class="lorem abs" style="left:45px;top:203px;width:90px;text-align:center;font-size:7px">To create your own, choose a topic that interests you.</p>
  <p class="lorem abs" style="left:169px;top:203px;width:90px;text-align:center;font-size:7px">To create your own, choose a topic that interests you.</p>
  <p class="lorem abs" style="left:293px;top:203px;width:90px;text-align:center;font-size:7px">To create your own, choose a topic that interests you.</p>
  <p class="lorem abs" style="left:417px;top:203px;width:90px;text-align:center;font-size:7px">To create your own, choose a topic that interests you.</p>
  <div class="footer">www.website.com</div>
</section>

<!-- 4 mission -->
<section class="slide c2 r2">
  <svg class="wedge" width="60" height="60"><polygon points="0,0 60,0 14,55 0,55" fill="var(--gold)"/></svg>
  <div class="num">4</div><div class="slide-title">Our Mission</div>
  <div class="brand-tag">LUMO STACK</div>
  <div class="bar-label" style="left:40px;top:84px;width:148px;padding-left:52px">TARGET</div>
  <div class="bar-label" style="left:207px;top:84px;width:160px;padding-left:52px">TARGET</div>
  <div class="bar-label" style="left:373px;top:84px;width:160px;padding-left:52px">TARGET</div>
  <svg class="abs" style="left:0;top:78px" width="545" height="40">
    <g fill="none" stroke="#fff" stroke-width="2">
      <circle cx="50" cy="19" r="19" fill="var(--navy)"/><circle cx="50" cy="19" r="11"/><circle cx="50" cy="19" r="4"/>
      <circle cx="217" cy="19" r="19" fill="var(--navy)"/><circle cx="217" cy="19" r="11"/><circle cx="217" cy="19" r="4"/>
      <circle cx="383" cy="19" r="19" fill="var(--navy)"/><circle cx="383" cy="19" r="11"/><circle cx="383" cy="19" r="4"/>
    </g>
  </svg>
  <p class="lorem abs" style="left:60px;top:130px;width:130px;text-align:center">Lorem ipsum dolor sit amet, consectetur adipiscing elit. Pellentesque eros quam, mattis condimentum ultrices sit amet, porttitor in quam.</p>
  <p class="lorem abs" style="left:213px;top:130px;width:130px;text-align:center">Lorem ipsum dolor sit amet, consectetur adipiscing elit. Pellentesque eros quam, mattis condimentum ultrices sit amet, porttitor in quam.</p>
  <p class="lorem abs" style="left:366px;top:130px;width:130px;text-align:center">Lorem ipsum dolor sit amet, consectetur adipiscing elit. Pellentesque eros quam, mattis condimentum ultrices sit amet, porttitor in quam.</p>
  <div class="skyline" role="img" aria-label="Faded city skyline"></div>
  <div class="footer">www.website.com</div>
</section>

<!-- 5 planning -->
<section class="slide c1 r3">
  <svg class="wedge" width="545" height="280">
    <polygon points="0,0 60,0 14,55 0,55" fill="var(--gold)"/>
    <polygon points="0,45 270,45 245,280 0,280" fill="var(--gold)"/>
  </svg>
  <div class="num">5</div><div class="slide-title">Our Planning</div>
  <div class="brand-tag">LUMO STACK</div>
  <div class="abs" style="left:10px;top:100px;width:215px;height:150px;background:linear-gradient(135deg,#e3c27a,#c98f2f);border-radius:6px" role="img" aria-label="Illustration of two business people presenting charts on a board"></div>
  <div class="list-item" style="top:87px"><b>1</b>Marketing Timing</div>
  <div class="list-item" style="top:118px"><b>2</b>Inappropriate advertising messages</div>
  <div class="list-item" style="top:148px"><b>3</b>Inappropriate way of promotion</div>
  <div class="list-item" style="top:178px"><b>4</b>Not Measuring Promotion Effectiveness</div>
  <div class="list-item" style="top:208px"><b>5</b>Lack of Communication with Consumers</div>
  <div class="footer">www.website.com</div>
</section>

<!-- 6 strategy -->
<section class="slide c2 r3">
  <svg class="wedge" width="60" height="60"><polygon points="0,0 60,0 14,55 0,55" fill="var(--gold)"/></svg>
  <div class="num">6</div><div class="slide-title">Our Strategy</div>
  <div class="brand-tag">LUMO STACK</div>
  <div class="icon-box" style="left:27px;top:96px"></div>
  <div class="abs" style="left:84px;top:96px;width:185px"><h3 class="gold">Increase employee satisfaction<br>and motivation</h3><p class="lorem" style="font-size:6px">Lorem ipsum dolor sit amet, consectetur adipiscing elit. Etiam convallis lacus elit, eu placerat tellus scelerisque a</p></div>
  <div class="icon-box" style="left:282px;top:96px"></div>
  <div class="abs" style="left:338px;top:96px;width:190px"><h3 class="gold">Preparing workers to assume new<br>responsibilities</h3><p class="lorem" style="font-size:6px">Lorem ipsum dolor sit amet, consectetur adipiscing elit. Etiam convallis lacus elit, eu placerat tellus scelerisque a</p></div>
  <div class="icon-box" style="left:27px;top:183px"></div>
  <div class="abs" style="left:84px;top:183px;width:185px"><h3 class="gold">A personal analysis for each<br>employee</h3><p class="lorem" style="font-size:6px">Lorem ipsum dolor sit amet, consectetur adipiscing elit. Etiam convallis lacus elit, eu placerat tellus scelerisque a</p></div>
  <div class="icon-box" style="left:282px;top:183px"></div>
  <div class="abs" style="left:338px;top:183px;width:190px"><h3 class="gold">Show employees that they are<br>valueable</h3><p class="lorem" style="font-size:6px">Lorem ipsum dolor sit amet, consectetur adipiscing elit. Etiam convallis lacus elit, eu placerat tellus scelerisque a</p></div>
  <div class="footer">www.website.com</div>
</section>

<!-- 7 opportunity -->
<section class="slide c1 r4">
  <svg class="wedge" width="60" height="60"><polygon points="0,0 60,0 14,55 0,55" fill="var(--gold)"/></svg>
  <div class="num">7</div><div class="slide-title">Opportunity</div>
  <div class="brand-tag">LUMO STACK</div>
  <svg class="abs" style="left:30px;top:70px" width="40" height="190">
    <g fill="none" stroke="var(--gold)" stroke-width="2"><circle cx="16" cy="16" r="14"/><circle cx="16" cy="58" r="14"/><circle cx="16" cy="100" r="14"/><circle cx="16" cy="146" r="14"/></g>
    <g fill="var(--ink)"><circle cx="16" cy="16" r="9"/><circle cx="16" cy="58" r="9"/><circle cx="16" cy="100" r="9"/><circle cx="16" cy="146" r="9"/></g>
  </svg>
  <div class="abs" style="left:70px;top:70px;width:220px"><h3 class="gold" style="font-weight:500;font-size:8px">Productivity</h3><p class="lorem" style="font-size:5.5px">Lorem ipsum dolor sit amet, consectetur adipiscing elit. Etiam convallis lacus elit, eu placerat tellus scelerisque a. Nulla non posuere nisi. Maecenas at tortor commodo, sollicitudin u.</p></div>
  <div class="abs" style="left:70px;top:112px;width:220px"><h3 class="gold" style="font-weight:500;font-size:8px">Loyality</h3><p class="lorem" style="font-size:5.5px">Lorem ipsum dolor sit amet, consectetur adipiscing elit. Etiam convallis lacus elit, eu placerat tellus scelerisque a. Nulla non posuere nisi. Maecenas at tortor commodo, sollicitudin u.</p></div>
  <div class="abs" style="left:70px;top:154px;width:220px"><h3 class="gold" style="font-weight:500;font-size:8px">Satisfaction</h3><p class="lorem" style="font-size:5.5px">Lorem ipsum dolor sit amet, consectetur adipiscing elit. Etiam convallis lacus elit, eu placerat tellus scelerisque a. Nulla non posuere nisi. Maecenas at tortor commodo, sollicitudin u.</p></div>
  <div class="abs" style="left:70px;top:200px;width:220px"><h3 class="gold" style="font-weight:500;font-size:8px">Public Trust</h3><p class="lorem" style="font-size:5.5px">Lorem ipsum dolor sit amet, consectetur adipiscing elit. Etiam convallis lacus elit, eu placerat tellus scelerisque a. Nulla non posuere nisi. Maecenas at tortor commodo, sollicitudin u.</p></div>
  <svg class="abs" style="left:320px;top:65px" width="210" height="200" font-family="Montserrat,sans-serif" font-size="6" fill="var(--text)">
    <line x1="36" y1="5" x2="36" y2="175" stroke="#bbb" stroke-width=".6"/>
    <text x="2" y="25">Item 1</text><text x="2" y="63">Item 2</text><text x="2" y="101">Item 3</text><text x="2" y="140">Item 4</text>
    <rect x="36" y="7" width="28" height="32" fill="var(--gold)"/><rect x="64" y="7" width="38" height="32" fill="#a9aaac"/><rect x="102" y="7" width="15" height="32" fill="var(--ink)"/>
    <rect x="36" y="45" width="41" height="32" fill="var(--gold)"/><rect x="77" y="45" width="38" height="32" fill="#a9aaac"/><rect x="115" y="45" width="29" height="32" fill="var(--ink)"/>
    <rect x="36" y="83" width="64" height="32" fill="var(--gold)"/><rect x="100" y="83" width="44" height="32" fill="#a9aaac"/><rect x="144" y="83" width="27" height="32" fill="var(--ink)"/>
    <rect x="36" y="121" width="75" height="32" fill="var(--gold)"/><rect x="111" y="121" width="54" height="32" fill="#a9aaac"/><rect x="165" y="121" width="33" height="32" fill="var(--ink)"/>
    <text x="34" y="186">0</text><text x="88" y="186">20</text><text x="142" y="186">40</text><text x="196" y="186">60</text>
  </svg>
  <div class="footer">www.website.com</div>
</section>

<!-- 8 about -->
<section class="slide c2 r4">
  <svg class="wedge" width="60" height="60"><polygon points="0,0 60,0 14,55 0,55" fill="var(--gold)"/></svg>
  <div class="num">8</div><div class="slide-title">About Us</div>
  <div class="brand-tag">LUMO STACK</div>
  <svg class="abs" style="left:52px;top:85px" width="60" height="130">
    <g fill="var(--gold)" stroke="#fff" stroke-width="2"><circle cx="28" cy="28" r="26"/><circle cx="28" cy="98" r="26"/></g>
    <g fill="#fff"><rect x="16" y="28" width="5" height="12"/><rect x="25" y="22" width="5" height="18"/><rect x="34" y="16" width="5" height="24"/>
    <rect x="16" y="98" width="5" height="12"/><rect x="25" y="92" width="5" height="18"/><rect x="34" y="86" width="5" height="24"/></g>
  </svg>
  <div class="abs" style="left:112px;top:86px;width:155px"><div style="font:600 11px 'Montserrat',sans-serif;color:var(--ink)">HISTORY</div><p class="lorem" style="font-size:6.5px">Lorem ipsum dolor sit amet, consectetur adipiscing elit. Aliquam tincidunt odio eu magna tristique gravida et in quam</p></div>
  <div class="abs" style="left:114px;top:155px;width:155px"><div style="font:600 11px 'Montserrat',sans-serif;color:var(--ink)">REVENUE</div><p class="lorem" style="font-size:6.5px">Lorem ipsum dolor sit amet, consectetur adipiscing elit. Aliquam tincidunt odio eu magna tristique gravida et in quam</p></div>
  <div class="stat" style="left:314px;top:78px">32</div>
  <div class="stat-cap" style="left:314px;top:124px">Years in the business</div>
  <div class="stat" style="left:307px;top:148px">$4B+</div>
  <div class="stat-cap" style="left:314px;top:194px">2026 Revenue</div>
  <div class="skyline" role="img" aria-label="Faded city skyline"></div>
  <div class="footer">www.website.com</div>
</section>

<!-- 9 testimonial -->
<section class="slide c1 r5" style="left:43px">
  <svg class="wedge" width="60" height="60"><polygon points="0,0 60,0 14,55 0,55" fill="var(--gold)"/></svg>
  <div class="num">9</div><div class="slide-title">Client Testimonial</div>
  <div class="brand-tag">LUMO STACK</div>
  <div class="photo" style="left:20px;top:102px;width:40px;height:40px;border-radius:50%" role="img" aria-label="Portrait of client Nora Lind"></div>
  <div class="quote-box" style="left:68px;top:85px"><strong>Nora Lind</strong><p>Lorem ipsum dolor sit amet, consectetur adipiscing elit. Cras lobortis vestibulum consectetur. Nunc euismod,</p></div>
  <div class="photo" style="left:273px;top:102px;width:40px;height:40px;border-radius:50%" role="img" aria-label="Portrait of client Tessa Vale"></div>
  <div class="quote-box" style="left:322px;top:85px"><strong>Tessa Vale</strong><p>Lorem ipsum dolor sit amet, consectetur adipiscing elit. Cras lobortis vestibulum consectetur. Nunc euismod,</p></div>
  <div class="skyline" role="img" aria-label="Faded city skyline"></div>
  <div class="footer">www.website.com</div>
</section>

<!-- 10 contact -->
<section class="slide c2 r5" style="left:612px">
  <svg class="wedge" width="60" height="60"><polygon points="0,0 60,0 14,55 0,55" fill="var(--gold)"/></svg>
  <div class="num" style="width:28px">10</div><div class="slide-title" style="left:56px">Contact Us</div>
  <div class="brand-tag">LUMO STACK</div>
  <div class="contact" style="top:78px"><i></i>+123-456-7890</div>
  <div class="contact" style="top:104px"><i></i>hello@lumostack.com</div>
  <div class="contact" style="top:132px"><i></i>www.lumostack.com</div>
  <div class="contact" style="top:160px;align-items:flex-start"><i style="margin-top:2px"></i><span>123 Anywhere St., Any City,<br>State, Country 12345</span></div>
  <div class="abs" style="left:315px;top:70px;width:62px;height:150px;background:var(--ink)"></div>
  <div class="photo" style="left:325px;top:78px;width:220px;height:126px;background:linear-gradient(180deg,#a9c6e0,#e9ecef 60%,#7f9a5a)" role="img" aria-label="Photo of a modern white villa with garden"></div>
  <div class="thanks">THANK YOU</div>
</section>

</body>
</html>
```